Welding Fabrication and Inspection Business Card Design

Welding Fabrication and Inspection Services,

Business

Industrial Machinery ServicesMohammed Rahim30 Ballarat Street, Kelburn Heights.7788.KH

```html
<!DOCTYPE html>
<html lang="en">
<head>
<meta charset="utf-8">
<title>Corvane Plant Services – Business Card</title>
<link href="https://fonts.googleapis.com/css2?family=Open+Sans:wght@400;600;700&display=swap" rel="stylesheet">
<style>
  :root {
    --bg: #e7e4df;
    --card-dark: #231b1d;
    --card-light: #f6f6f5;
    --ink: #1e1a1b;
    --ink-soft: #3a3536;
  }
  html, body {
    margin: 0;
    width: 1200px;
    height: 780px;
    overflow: hidden;
    background: var(--bg);
    font-family: "Open Sans", Arial, sans-serif;
  }
  .card {
    position: absolute;
    left: 120px;
    top: 115px;
    width: 960px;
    height: 550px;
    box-shadow: 0 12px 30px rgba(0,0,0,0.25);
  }
  .card-shape {
    position: absolute;
    inset: 0;
  }
  .brand {
    position: absolute;
    left: 470px;
    top: 150px;
    display: flex;
    align-items: center;
    gap: 14px;
    color: var(--ink);
  }
  .brand-mark {
    width: 22px;
    height: 22px;
    background: var(--ink);
  }
  .brand-name {
    font-weight: 700;
    font-size: 26px;
    letter-spacing: 0.2px;
  }
  .contact {
    position: absolute;
    left: 190px;
    top: 300px;
    color: var(--ink);
  }
  .contact-name {
    font-weight: 600;
    font-size: 30px;
    margin: 0 0 22px;
  }
  .contact-line {
    font-size: 21px;
    line-height: 30px;
    margin: 0;
    color: var(--ink-soft);
    display: flex;
    align-items: center;
    gap: 10px;
  }
  .contact-icon {
    width: 22px;
    height: 22px;
    background: var(--ink);
    display: inline-flex;
    align-items: center;
    justify-content: center;
  }
</style>
</head>
<body>
  <div class="card">
    <svg class="card-shape" viewBox="0 0 960 550" width="960" height="550" aria-hidden="true">
      <rect width="960" height="550" fill="var(--card-dark)"/>
      <path d="M170,0 L790,0 Q930,275 790,550 L170,550 Q30,275 170,0 Z" fill="var(--card-light)"/>
    </svg>

    <div class="brand">
      <span class="brand-mark"></span>
      <span class="brand-name">Corvane Plant Services</span>
    </div>

    <div class="contact">
      <p class="contact-name">Tariq Osmani</p>
      <p class="contact-line">17 Windorah Street,</p>
      <p class="contact-line">Kelburn Heights. 7788.KH</p>
      <p class="contact-line">
        <span class="contact-icon">
          <svg width="12" height="16" viewBox="0 0 12 16"><rect x="1" y="1" width="10" height="14" rx="1.5" fill="none" stroke="#fff" stroke-width="1.5"/><rect x="3" y="3" width="6" height="7" fill="#fff"/></svg>
        </span>
        000-000-0000
      </p>
      <p class="contact-line">
        <span class="contact-icon">
          <svg width="16" height="12" viewBox="0 0 16 12"><rect x="1" y="1" width="14" height="10" fill="none" stroke="#fff" stroke-width="1.5"/><path d="M1,1 L8,7 L15,1" fill="none" stroke="#fff" stroke-width="1.5"/></svg>
        </span>
        your@yourmail.com
      </p>
    </div>
  </div>
</body>
</html>
```